Kestrelbay Racquet Club app

Design a sporting app that can, post news, post events, capture and show live scores, link at least 6 websites, other functions would be an advantage. Real tennis is also known as Royal tennis and Court tennis.
This would be like a sporting clubs app that gives live scores.

Colors

Designer to choose colors to be used in the design.

Requirements
Must have
• post news, post events, capture and show live scores, link at least 6 websites,
Nice to have
• Instructions on how to launch the app on apple and android

```html
<!DOCTYPE html>
<html lang="en">
<head>
<meta charset="utf-8">
<title>Kestrelbay Racquet Club — News</title>
<link href="https://fonts.googleapis.com/css2?family=Open+Sans:wght@400;600;700;800&display=swap" rel="stylesheet">
<style>
  :root {
    --navy: #16178f;
    --royal: #1c2bc0;
    --bright: #2147de;
    --ink: #111111;
    --link: #1f4fe0;
    --white: #ffffff;
    --card-shadow: rgba(5, 10, 70, 0.35);
  }
  * { margin: 0; padding: 0; box-sizing: border-box; }
  html, body { width: 1200px; height: 2598px; overflow: hidden; }
  body {
    font-family: "Open Sans", sans-serif;
    color: var(--white);
    background: linear-gradient(180deg, var(--navy) 0%, var(--royal) 50%, var(--bright) 100%);
    position: relative;
  }
  .diagonal-band {
    position: absolute; inset: 0;
    background: linear-gradient(125deg, transparent 0%, transparent 55%, rgba(255,255,255,0.05) 55%, rgba(255,255,255,0.05) 100%),
                linear-gradient(55deg, rgba(255,255,255,0.06) 0%, rgba(255,255,255,0.06) 18%, transparent 18%);
  }
  .hero-photo {
    position: absolute; left: 0; top: 0; width: 1200px; height: 939px;
    background:
      linear-gradient(180deg, rgba(28,30,160,0.85) 0%, rgba(70,90,200,0.45) 25%, rgba(60,70,180,0.6) 55%, rgba(30,40,170,0.95) 92%, var(--royal) 100%),
      linear-gradient(180deg, #b8c6ee 0%, #8fa4dc 40%, #3f5a6a 65%, #4a55a8 100%);
  }
  .status-bar { position: absolute; left: 0; top: 0; width: 1200px; height: 90px; }
  .status-time { position: absolute; left: 85px; top: 28px; font-size: 22px; font-weight: 600; }
  .status-icons { position: absolute; right: 82px; top: 32px; }
  .page-title-ghost {
    position: absolute; left: 0; width: 1200px; top: 110px; text-align: center;
    font-size: 170px; font-weight: 800; letter-spacing: -4px; color: rgba(255,255,255,0.08);
  }
  .page-title {
    position: absolute; left: 0; width: 1212px; top: 160px; text-align: center;
    font-size: 112px; font-weight: 700; letter-spacing: -4px; line-height: 1;
  }
  .carousel-shade { position: absolute; top: 1020px; }
  .carousel-arrow { position: absolute; top: 1142px; }
  .feature-card {
    position: absolute; top: 939px; width: 451px; height: 539px;
    background: var(--white); border-radius: 8px; overflow: hidden;
    box-shadow: 0 10px 30px var(--card-shadow); color: var(--ink);
  }
  .feature-card__image { height: 362px; }
  .feature-card__body { padding: 26px 35px 0; }
  .feature-card__title { font-size: 19.5px; font-weight: 700; letter-spacing: -0.3px; }
  .feature-card__text { font-size: 17px; line-height: 27px; margin-top: 10px; }
  .feature-card__link { display: block; margin-top: 8px; font-size: 17px; font-weight: 700; color: var(--link); text-decoration: none; }
  .section-heading {
    position: absolute; left: 49px; top: 1540px; font-size: 39px; font-weight: 700; letter-spacing: -0.5px;
  }
  .headline-story {
    position: absolute; left: 43px; top: 1629px; width: 1115px; height: 480px; overflow: hidden;
    box-shadow: 0 10px 30px var(--card-shadow);
  }
  .headline-story__image {
    position: absolute; inset: 0;
    background: linear-gradient(180deg, #2c3f9a 0%, #35559e 30%, #2a3e9e 55%, #2135c4 85%, #2236c8 100%);
  }
  .headline-story__title { position: absolute; left: 47px; top: 1988px; }
  .headline-story__title, .headline-story__sub { position: absolute; left: 47px; }
  .headline-story__title { top: 356px; font-size: 34px; font-weight: 700; letter-spacing: -0.4px; }
  .headline-story__sub { top: 410px; font-size: 28px; font-weight: 400; letter-spacing: 0.5px; }
  .news-item { position: absolute; top: 2206px; width: 560px; height: 240px; }
  .news-item__image { position: absolute; left: 0; top: 0; width: 239px; height: 239px; border-radius: 6px; }
  .news-item__body { position: absolute; left: 271px; top: 18px; width: 290px; }
  .news-item__title { font-size: 21px; font-weight: 700; line-height: 31px; letter-spacing: -0.3px; }
  .news-item__text { margin-top: 14px; font-size: 18.5px; line-height: 27px; }
  .news-item__link { display: block; margin-top: 16px; font-size: 18.5px; font-weight: 700; color: var(--white); text-decoration: none; }
</style>
</head>
<body>
  <div class="diagonal-band"></div>

  <div class="hero-photo" role="img" aria-label="Tennis player serving on an outdoor court under a cloudy sky, tinted blue"></div>

  <div class="status-bar">
    <span class="status-time">9:41</span>
    <svg class="status-icons" width="110" height="24" viewBox="0 0 110 24">
      <g fill="#fff">
        <rect x="0" y="14" width="4" height="6" rx="1"/>
        <rect x="7" y="11" width="4" height="9" rx="1"/>
        <rect x="14" y="7" width="4" height="13" rx="1"/>
        <rect x="21" y="3" width="4" height="17" rx="1"/>
        <path d="M44 20 l-4 -5 a7 7 0 0 1 8 0 z"/>
        <path d="M35 10 a13 13 0 0 1 18 0 l-2.5 2.5 a9.5 9.5 0 0 0 -13 0 z"/>
        <path d="M31 6 a19 19 0 0 1 26 0 l-2.5 2.5 a15.5 15.5 0 0 0 -21 0 z"/>
        <rect x="70" y="4" width="36" height="17" rx="4" fill="none" stroke="#fff" stroke-width="2"/>
        <rect x="73" y="7" width="30" height="11" rx="2"/>
        <rect x="107" y="9" width="2.5" height="7" rx="1"/>
      </g>
    </svg>
  </div>

  <div class="page-title-ghost">NEWS</div>
  <h1 class="page-title">NEWS</h1>

  <svg class="carousel-shade" style="left:10px" width="140" height="240" viewBox="0 0 140 240"><path d="M130 0 L0 120 L130 240 Z" fill="rgba(10,15,110,0.35)"/></svg>
  <svg class="carousel-shade" style="left:1050px" width="140" height="240" viewBox="0 0 140 240"><path d="M10 0 L140 120 L10 240 Z" fill="rgba(10,15,110,0.35)"/></svg>
  <svg class="carousel-arrow" style="left:64px" width="26" height="46" viewBox="0 0 26 46"><path d="M22 4 L5 23 L22 42" fill="none" stroke="#fff" stroke-width="5" stroke-linecap="round" stroke-linejoin="round"/></svg>
  <svg class="carousel-arrow" style="left:1126px" width="26" height="46" viewBox="0 0 26 46"><path d="M4 4 L21 23 L4 42" fill="none" stroke="#fff" stroke-width="5" stroke-linecap="round" stroke-linejoin="round"/></svg>

  <article class="feature-card" style="left:143px">
    <div class="feature-card__image" role="img" aria-label="Silver championship trophy cup in front of a wooden fence" style="background:linear-gradient(180deg,#3d4a2c 0%,#6b4a34 35%,#9a9aa0 60%,#5a4030 100%)"></div>
    <div class="feature-card__body">
      <h3 class="feature-card__title">LOREM IPSUM IS SIMPLY DUMMY TEXT</h3>
      <p class="feature-card__text">printing and typesetting industry. Lorem Ipsum has been the industry's</p>
      <a class="feature-card__link" href="#">Read More</a>
    </div>
  </article>

  <article class="feature-card" style="left:635px">
    <div class="feature-card__image" role="img" aria-label="Club house and palm tree beside a green lawn under a blue sky" style="background:linear-gradient(180deg,#4f8fe0 0%,#7fb1ee 40%,#9b7a5c 55%,#6f8a3c 70%,#8a9a4a 100%)"></div>
    <div class="feature-card__body">
      <h3 class="feature-card__title">LOREM IPSUM IS SIMPLY DUMMY TEXT</h3>
      <p class="feature-card__text">printing and typesetting industry. Lorem Ipsum has been the industry's</p>
      <a class="feature-card__link" href="#">Read More</a>
    </div>
  </article>

  <h2 class="section-heading">LATEST NEWS</h2>

  <article class="headline-story">
    <div class="headline-story__image" role="img" aria-label="Club entrance sign welcoming visitors, tinted blue"></div>
    <h3 class="headline-story__title">LOREM IPSUM IS SIMPLY DUMMY TEXT OF THE</h3>
    <p class="headline-story__sub">Lorem Ipsum is simply dummy text</p>
  </article>

  <article class="news-item" style="left:44px">
    <div class="news-item__image" role="img" aria-label="Two wooden tennis racquets and a ball resting against a bench on grass" style="background:linear-gradient(160deg,#6e7a55 0%,#a9a58a 45%,#5f8040 100%)"></div>
    <div class="news-item__body">
      <h3 class="news-item__title">LOREM IPSUM IS SIMPLY DUMMY TEXT</h3>
      <p class="news-item__text">printing and typesetting industry. Lorem Ipsum has been the industry's</p>
      <a class="news-item__link" href="#">Read More</a>
    </div>
  </article>

  <article class="news-item" style="left:630px">
    <div class="news-item__image" role="img" aria-label="Tennis net on an orange clay court" style="background:linear-gradient(120deg,#3a3a30 0%,#6a4a30 35%,#d86a2a 60%,#e07a30 100%)"></div>
    <div class="news-item__body">
      <h3 class="news-item__title">LOREM IPSUM IS SIMPLY DUMMY TEXT</h3>
      <p class="news-item__text">printing and typesetting industry. Lorem Ipsum has been the industry's</p>
      <a class="news-item__link" href="#">Read More</a>
    </div>
  </article>
</body>
</html>
```